Brightpath Holdings Business Card

Create a two sided, high gloss, quality business card for Brightpath Holdings.

Target Market(s)

People wanting to purchase, scale, and sell businesses.

Industry/Entity Type

Entrepreneurs

Contact Information for Business Card

One line: Dana Velko, CPA, CMA Another line: Entrepreneur & Investor Another line: Business Ownership Transition Expert Another line: Multi-State Licensed Real Estate Broker Phone 954-BRTPATH (278-7284) Email Dana@Brightpath Holdings.example Website www.Brightpath.example

Requirements
Must have
• Black Card, logo on one side, all other information on the other side including a small logo.
Nice to have
• Possibly add a tagline "Helping entrepreneurs live a life they don't need a vacation from"
Should not have
• There will not be a mailing address on these cards.

```html
<!DOCTYPE html>
<html lang="en">
<head>
<meta charset="utf-8">
<title>Brightpath Holdings Business Card</title>
<link href="https://fonts.googleapis.com/css2?family=Montserrat:wght@400;500;600&display=swap" rel="stylesheet">
<style>
  :root {
    --backdrop: #e9e9ea;
    --card-black: #0b0b0c;
    --gold: #d6a93e;
    --gold-light: #e8c562;
    --text-white: #ececec;
    --photo-top: #3a2a20;
    --photo-bottom: #1c1f2a;
  }
  * { margin: 0; padding: 0; box-sizing: border-box; }
  html, body { width: 900px; height: 1200px; overflow: hidden; }
  body {
    background: var(--backdrop);
    font-family: "Montserrat", sans-serif;
    position: relative;
  }
  .card {
    position: absolute;
    left: 135px;
    width: 630px;
    height: 357px;
    background: var(--card-black);
    border-radius: 12px;
    overflow: hidden;
  }
  .card-front { top: 215px; }
  .card-back { top: 628px; }

  .brand {
    position: absolute;
    display: flex;
    align-items: center;
    color: var(--gold);
    font-weight: 600;
    white-space: nowrap;
  }
  .brand-dot {
    border-radius: 50%;
    background: var(--gold);
    flex: none;
  }
  .card-front .brand {
    left: 0; right: 0; top: 150px;
    justify-content: center;
    font-size: 40px;
    gap: 16px;
  }
  .card-front .brand-dot { width: 26px; height: 26px; }
  .card-back .brand {
    left: 33px; top: 60px;
    font-size: 24px;
    gap: 10px;
  }
  .card-back .brand-dot { width: 16px; height: 16px; }

  .holder-name {
    position: absolute;
    left: 38px; top: 150px;
    color: var(--gold-light);
    font-size: 21px;
    font-weight: 500;
    letter-spacing: 0.5px;
  }
  .holder-roles {
    position: absolute;
    left: 38px; top: 182px;
    list-style: none;
    color: var(--text-white);
    font-size: 14px;
    line-height: 20px;
    letter-spacing: 0.6px;
  }
  .contact-list {
    position: absolute;
    left: 38px; top: 262px;
    list-style: none;
    color: var(--text-white);
    font-size: 14px;
    line-height: 22px;
    letter-spacing: 0.4px;
  }
  .contact-list li { display: flex; align-items: center; gap: 7px; }
  .contact-icon { width: 11px; height: 11px; fill: var(--gold); flex: none; }

  .portrait {
    position: absolute;
    left: 356px; top: 32px;
    width: 274px; height: 325px;
    background: linear-gradient(180deg, var(--photo-top) 0%, #4a3528 45%, var(--photo-bottom) 100%);
    border-radius: 120px 120px 0 0;
  }
</style>
</head>
<body>
  <section class="card card-front">
    <div class="brand"><span class="brand-dot"></span>Brightpath Holdings</div>
  </section>

  <section class="card card-back">
    <div class="brand"><span class="brand-dot"></span>Brightpath Holdings</div>
    <h1 class="holder-name">Dana Velko, CPA, CMA</h1>
    <ul class="holder-roles">
      <li>Entrepreneur &amp; Investor</li>
      <li>Business Ownership Transition Expert</li>
      <li>Multi-State Licensed Real Estate Broker</li>
    </ul>
    <ul class="contact-list">
      <li>
        <svg class="contact-icon" viewBox="0 0 24 24"><path d="M6.6 10.8a15.1 15.1 0 0 0 6.6 6.6l2.2-2.2c.3-.3.7-.4 1-.2 1.1.4 2.3.6 3.6.6.6 0 1 .4 1 1V20c0 .6-.4 1-1 1A17 17 0 0 1 3 4c0-.6.4-1 1-1h3.5c.6 0 1 .4 1 1 0 1.3.2 2.5.6 3.6.1.3 0 .7-.2 1z"/></svg>
        954-BRTPATH (278-7284)
      </li>
      <li>
        <svg class="contact-icon" viewBox="0 0 24 24"><path d="M2 5h20v14H2z M2 5l10 8 10-8" fill="var(--gold)"/><path d="M2 5l10 8 10-8" fill="none" stroke="#0b0b0c" stroke-width="2"/></svg>
        Dana@Brightpath Holdings.example
      </li>
      <li>
        <svg class="contact-icon" viewBox="0 0 24 24"><circle cx="12" cy="12" r="10" fill="none" stroke="var(--gold)" stroke-width="2"/><path d="M2 12h20M12 2c3 3 3 17 0 20M12 2c-3 3-3 17 0 20" fill="none" stroke="var(--gold)" stroke-width="1.6"/></svg>
        www.Brightpath.example
      </li>
    </ul>
    <div class="portrait" role="img" aria-label="Portrait photo of Dana Velko in a dark blazer and yellow blouse"></div>
  </section>
</body>
</html>
```